Ridgeline Orchards Organic Cherry POS card 7x11

We are wanting to create a one-sided 7 x 11 organic cherry card that is eye catching and informative.This should be clear and easy to read and not cluttered. We use these cards as a display in grocery stores, demo stands, and other events to market Organic Ridgeline Sweet Orchards. We have a few facts that we would like displayed on the card (see attachment).

Target Market(s)

Consumers

Industry/Entity Type

Agriculture

Requirements
Must have
• Natural color palettes
• Easy to read
• Ridgeline Orchards
Nice to have
• Unique, realistic cherry design

```html
<!DOCTYPE html>
<html lang="en">
<head>
<meta charset="utf-8">
<title>Ridgeline Orchards – Organic Cherry Card</title>
<link rel="stylesheet" href="https://fonts.googleapis.com/css2?family=Archivo+Black&display=swap">
<style>
  :root {
    --cherry-deep: #5a0610;
    --cherry-mid: #a3111f;
    --cherry-bright: #d8243a;
    --panel-white: #ffffff;
    --ink: #1b1b1b;
    --mark-red: #7a0d1c;
    --text-white: #ffffff;
    --text-edge: #000000;
  }
  html, body {
    margin: 0;
    padding: 0;
    width: 798px;
    height: 1200px;
    overflow: hidden;
    background: #ffffff;
  }
  .card {
    position: relative;
    width: 798px;
    height: 1200px;
    overflow: hidden;
    font-family: "Archivo Black", "Arial Black", sans-serif;
  }
  .cherry-backdrop {
    position: absolute;
    inset: 0;
    background:
      radial-gradient(ellipse at 30% 20%, var(--cherry-bright) 0%, transparent 55%),
      radial-gradient(ellipse at 75% 60%, var(--cherry-bright) 0%, transparent 50%),
      radial-gradient(ellipse at 20% 85%, var(--cherry-mid) 0%, transparent 55%),
      linear-gradient(160deg, var(--cherry-mid) 0%, var(--cherry-deep) 100%);
  }
  .brand-panel {
    position: absolute;
    left: 88px;
    top: 72px;
    width: 614px;
    height: 214px;
    background: var(--panel-white);
    display: flex;
    align-items: center;
    justify-content: center;
    gap: 22px;
  }
  .brand-dot {
    width: 64px;
    height: 64px;
    border-radius: 50%;
    background: var(--mark-red);
    flex: none;
  }
  .brand-name {
    font-size: 44px;
    color: var(--ink);
    letter-spacing: 0.5px;
    white-space: nowrap;
  }
  .fact {
    position: absolute;
    left: 96px;
    margin: 0;
    font-size: 38px;
    line-height: 51px;
    color: var(--text-white);
    white-space: nowrap;
    text-shadow:
      -2px -2px 0 var(--text-edge), 2px -2px 0 var(--text-edge),
      -2px 2px 0 var(--text-edge), 2px 2px 0 var(--text-edge),
      0 0 6px rgba(0,0,0,0.6);
  }
  .fact--share { top: 356px; }
  .fact--state { top: 560px; }
  .benefits { top: 760px; }
  .benefits span { display: block; }
</style>
</head>
<body>
  <main class="card">
    <div class="cherry-backdrop" role="img" aria-label="Photograph of a heap of fresh red sweet cherries filling the card"></div>

    <header class="brand-panel">
      <span class="brand-dot"></span>
      <span class="brand-name">Ridgeline Orchards</span>
    </header>

    <p class="fact fact--share">Organic Ridgeline cherries<br>make up 1/3 of the<br>nation’s production.</p>

    <p class="fact fact--state">Washington State is the<br>nation’s largest producer of<br>organic cherries.</p>

    <p class="fact benefits">
      <span>Health benefits:</span>
      <span>Fat Free</span>
      <span>Source of Vitamin C</span>
      <span>A Natural Anti-Inflammatory</span>
      <span>Source of Potassium</span>
      <span>Source of Melatonin</span>
    </p>
  </main>
</body>
</html>
```